Corvell Ashdown Website

Updated website for Corvell Ashdown Dry Cleaners & Garment Care.

Please look at www.tindalepressers.example we really like this site!!!

We are not set on colors or fonts. Looking for an professional easy to use site that looks and works even better on a mobile device. 90% of our customers visit us on cell phones.

Target Market(s)

We are located in an up scale area with young trendy individuals but, also very successful mature customers as well. Probably geared more to tech savvy younger crowd.

Industry/Entity Type

Dry Cleaning

Coding

Coded - Design and coding required

Font styles to use
Serif
Script

Colors
85abd2
85cae6
cee9f5
cfdeed
757575

Requirements
Must have
• Must look good on a mobile device and have sign up for our pick up and delivery. Geographical pick up and delivery perimeters would be great as well. Capturing emails and other user data for future marketing. We do a lot of advertising.
• Please look at www.tindalepressers.example we really like this site!!!
• Search engine optimized.
• Also we are adding a new POS system that will have a login for customers and possibly an app.
Nice to have
• 100% satisfaction guaranteed and scrolling reviews somewhere on the page.

```html
<!DOCTYPE html>
<html lang="en">
<head>
<meta charset="utf-8">
<title>Corvell Ashdown Dry Cleaning &amp; Garment Experts</title>
<link rel="stylesheet" href="https://fonts.googleapis.com/css2?family=Source+Sans+3:wght@400;600;700;800&display=swap">
<style>
  :root {
    --navy: #17296b;
    --white: #ffffff;
    --ink: #1d2240;
    --muted: #6b6f7a;
    --rule: #e3e4e8;
    --hero-top: #5a6a93;
    --hero-bottom: #44547f;
  }
  * { margin: 0; padding: 0; box-sizing: border-box; }
  html, body { width: 1200px; height: 683px; overflow: hidden; }
  body { font-family: "Source Sans 3", sans-serif; background: var(--white); position: relative; }

  .site-header { position: absolute; top: 0; left: 0; width: 1200px; height: 83px; background: var(--white); z-index: 2; }
  .brand-box {
    position: absolute; left: 150px; top: 0; width: 134px; height: 115px;
    background: var(--navy); display: flex; align-items: flex-end; justify-content: center;
    padding-bottom: 18px;
  }
  .brand-name { color: var(--white); font-weight: 700; font-size: 10px; letter-spacing: 0.3px; text-transform: uppercase; }

  .topbar {
    position: absolute; right: 146px; top: 7px; width: 290px; height: 23px;
    border-bottom: 1px solid var(--rule);
    display: flex; justify-content: flex-end; align-items: center; gap: 20px;
    font-size: 9.5px; padding-right: 12px;
  }
  .topbar-address { color: var(--muted); display: flex; align-items: center; gap: 4px; }
  .topbar-phone { color: var(--ink); }

  .main-nav { position: absolute; left: 454px; top: 37px; height: 38px; display: flex; align-items: center; }
  .main-nav a { color: var(--ink); text-decoration: none; font-size: 11.5px; letter-spacing: 1px; margin-right: 25px; }
  .main-nav .nav-cta {
    margin: 0 0 0 -1px; background: var(--navy); color: var(--white); font-weight: 700;
    width: 170px; height: 38px; display: flex; align-items: center; justify-content: center; letter-spacing: 1.6px;
  }

  .hero { position: absolute; left: 0; top: 83px; width: 1200px; height: 600px; }
  .hero-photo { position: absolute; inset: 0; background: linear-gradient(160deg, var(--hero-top), var(--hero-bottom)); }
  .hero-content { position: absolute; left: 166px; top: 100px; color: var(--white); }
  .hero-title { font-weight: 800; font-size: 50px; line-height: 55px; letter-spacing: -0.3px; }
  .hero-text { margin-top: 22px; width: 500px; font-size: 15px; line-height: 23.5px; letter-spacing: -0.2px; }
  .hero-actions { position: absolute; top: 395px; left: 166px; display: flex; gap: 20px; }
  .btn {
    height: 48px; display: flex; align-items: center; justify-content: center;
    font-size: 11.5px; font-weight: 800; letter-spacing: 4.2px; color: var(--white); text-transform: uppercase;
  }
  .btn-solid { width: 224px; background: var(--navy); }
  .btn-outline { width: 202px; border: 2px solid var(--white); }
</style>
</head>
<body>
  <header class="site-header">
    <div class="brand-box"><span class="brand-name">Corvell Ashdown</span></div>
    <div class="topbar">
      <span class="topbar-address">
        <svg width="10" height="9" viewBox="0 0 10 9" aria-hidden="true"><path d="M5 0 L10 4.5 H8.6 V9 H6 V6 H4 V9 H1.4 V4.5 H0 Z" fill="#8a8d96"/></svg>
        2217 E Linden Ave, Brenmoor, MN 55820
      </span>
      <span class="topbar-phone">(555) 014-2290</span>
    </div>
    <nav class="main-nav">
      <a href="#">HOME</a>
      <a href="#">ABOUT</a>
      <a href="#">OUR SERVICES</a>
      <a href="#">COVERAGE AREA</a>
      <a href="#">CONTACT US</a>
      <a href="#" class="nav-cta">SCHEDULE PICKUP</a>
    </nav>
  </header>

  <section class="hero">
    <div class="hero-photo" role="img" aria-label="Close-up of a person in a striped blue shirt fastening a cuff, wearing a wristwatch, under a navy tint"></div>
    <div class="hero-content">
      <h1 class="hero-title">Because your<br>garments deserve<br>only the best</h1>
      <p class="hero-text">Corvell Ashdown Dry Cleaning &amp; Garment Experts is a family-owned business with over 50 years of experience in offering you an exceptional quality and service of dry cleaning and garment care.</p>
    </div>
    <div class="hero-actions">
      <a class="btn btn-solid">Schedule Pickup</a>
      <a class="btn btn-outline">Coverage Area</a>
    </div>
  </section>
</body>
</html>
```